Web Design Project for Communications Agency

The design I need (PSD file) is for an agency offering specialised PR and communications services for customers in the healthcare sector.

OBJECTIVES OF THE WEBSITE:
1. To promote the agency's communication services
2. To position Pellerin Dautry as an industry leader, an expert in healthcare PR and communications by highlighting blogposts and social media.

WHAT I NEED:
1st, I need the design for the Home Page ONLY.
Once approved, I will need the other pages designed as well. (Here is prototype that we've already developed for the Website that will guide you in the design:
http://velocraft.example/pellerindautry/)

VISUAL INSPIRATION
We want to give this Website a "Flat Design" look. Here are some websites for inspiration :
- http://marbleforge.example/#!/process
- http://www.brisklane.example/
- http://tovalinework.example/

Also, reuse images found on the company's current Website :
http://www.pellerindautry.example/fr/index.html

HOMEPAGE MAIN ELEMENTS:
1. Main menu : 6 sections
Accueil | Agence | Services | Approche | Publications | Contact

2. Main Call To Action (big dark rectangle in prototype):
Can be slider or just an information bloc.

3. Publications récentes :
The 4 latest blog posts must be features on the homepage (will be linked with the "Publications" section)

4. Dynamic Footer :
Contains a Chirplet feed and a Subscribe to our Newsletter feature (revecez nos publications)

OTHER PAGES (to design once Homepage is approved)
- Agence (about us)
- Services (our team)
- Approche (our approach)
- Publications (blog articles)
- Contact (Contact us)

• Please refer to prototype :
http://velocraft.example/pellerindautry/
Must have ALL features present in prototype.

Also, must reuse this picture in the design : http://pellerindautry.example/static/images/home-big-box.jpg

Finally, you will find attached the company logo.

```html
<!DOCTYPE html>
<html lang="en">
<head>
<meta charset="utf-8">
<title>Pellerin Dautry – Accueil</title>
<link href="https://fonts.googleapis.com/css2?family=Roboto+Condensed:wght@400;700&family=Open+Sans:wght@400;600;700&family=Raleway:wght@300;800&display=swap" rel="stylesheet">
<style>
:root{
  --red:#e2353b;
  --ink:#333333;
  --muted:#666666;
  --light:#efefef;
  --white:#ffffff;
  --band:#3a3a3a;
  --rule:#d9d9d9;
}
*{margin:0;padding:0;box-sizing:border-box}
html,body{width:676px;height:1200px;overflow:hidden;background:var(--white)}
body{position:relative;font-family:"Open Sans",Arial,sans-serif;color:var(--ink)}
.abs{position:absolute}

/* header */
.topbar{left:0;top:0;width:676px;height:58px;background:var(--light)}
.phone{right:22px;top:16px;display:flex;align-items:center;gap:8px;font-family:"Roboto Condensed",sans-serif;font-style:italic;font-size:22px;color:var(--red);letter-spacing:.5px}
.navband{left:0;top:58px;width:676px;height:50px;background:var(--white)}
.nav{left:0;top:58px;width:676px;height:50px;font-family:"Roboto Condensed",sans-serif;font-size:14px;color:#888}
.nav a{position:absolute;top:14px;color:inherit;text-decoration:none;white-space:nowrap;line-height:18px}
.nav a.active{color:var(--ink);top:7px;padding:7px 6px;border-top:2px solid var(--red);border-bottom:2px solid var(--red)}
.nav .n1{left:185px}
.nav .n2{left:274px}
.nav .n3{left:348px}
.nav .n4{left:482px}
.nav .n5{left:582px}
.brandtag{left:33px;top:0;width:133px;height:160px;background:var(--white);clip-path:polygon(0 0,100% 0,100% 100%,50% 88%,0 100%);display:flex;flex-direction:column;align-items:center;padding-top:18px}
.brandname{font-family:"Roboto Condensed",sans-serif;font-weight:400;color:var(--red);font-size:27px;line-height:25px;text-align:center}

/* hero */
.hero{left:0;top:122px;width:676px;height:290px;background:linear-gradient(100deg,#6d5a4c 0%,#3c2f28 45%,#241c18 100%)}
.hero-box{left:48px;top:160px;width:254px;height:245px;background:linear-gradient(150deg,#fafafa 0%,#e9e9e9 60%,#cfcfcf 100%);clip-path:polygon(0 12%,55% 0,100% 35%,80% 100%,30% 95%,5% 60%)}
.hero-title{left:342px;top:172px;width:320px;font-family:"Raleway",sans-serif;font-size:30px;line-height:38px;color:var(--white);font-weight:800;white-space:nowrap}
.hero-title .thin{font-weight:300}
.hero-title .hl{color:var(--red)}

/* services */
.section-head{left:19px;top:424px;width:638px;display:flex;align-items:center;gap:8px;font-family:"Roboto Condensed",sans-serif;font-weight:700;font-size:19px;color:var(--red)}
.section-head::after{content:"";flex:1;height:1px;background:var(--red)}
.tiles{left:19px;top:460px;width:638px;display:grid;grid-template-columns:repeat(4,150px);grid-template-rows:131px 131px;column-gap:12.6px;row-gap:13px}
.tile-feature{background:var(--red);color:var(--white);font-family:"Roboto Condensed",sans-serif;font-size:17px;line-height:23px;padding:52px 0 0 28px}
.t1{background:linear-gradient(160deg,#c9c9c9,#f2f2f2 55%,#8d8d9a)}
.t2{background:radial-gradient(circle at 60% 55%,#8e8e8e,#2b2b2b 70%)}
.t3{background:linear-gradient(170deg,#e8e8e8,#b9b0a8 70%,#5c4a3e)}
.t4{background:linear-gradient(180deg,#cfcfcf,#9a9a9a)}
.t5{background:radial-gradient(circle at 50% 50%,#d4d4d4,#8f8f8f)}
.t6{background:linear-gradient(180deg,#3a1a16,#8a4a38 50%,#2a1410)}
.t7{background:linear-gradient(180deg,#c7c2bf,#8b6a5b)}

/* contact band */
.contact{left:0;top:746px;width:676px;height:154px;background:var(--band)}
.map{left:20px;top:753px;width:309px;height:138px;background:linear-gradient(120deg,#e9e6df 0%,#dfe6d6 45%,#b9cdea 70%,#e9e6df 100%)}
.cinfo{left:342px;top:766px;width:325px;color:var(--white);font-size:8.5px}
.crow{display:flex;align-items:center;gap:8px;margin-bottom:9px;white-space:nowrap}
.people{display:flex;gap:10px;margin-top:20px}
.person{width:150px}
.pname{color:var(--red);font-size:9px;text-transform:uppercase;margin-bottom:6px;padding-left:16px}
.prole{margin-bottom:6px;padding-left:16px}
.icon{flex:none}

/* footer columns */
.col{top:912px;width:192px}
.col-tweets{left:26px}
.col-posts{left:242px}
.col-follow{left:460px}
.col-title{font-family:"Roboto Condensed",sans-serif;font-size:18px;color:var(--red);padding-bottom:5px;border-bottom:1px solid var(--red);margin-bottom:10px}
.tweet{display:flex;gap:10px;font-size:7.5px;line-height:11.5px;color:var(--muted);padding-bottom:4px;margin-bottom:5px;border-bottom:1px solid var(--rule)}
.tweet:last-of-type{border-bottom:none}
.avatar-brand{width:28px;flex:none;font-family:"Roboto Condensed",sans-serif;color:var(--red);font-size:8px;line-height:8px;padding-top:2px}
.tweet b{color:var(--ink);font-size:8px}
.tweet a{color:var(--red)}
.tweet .date{color:var(--ink)}
.follow-tw{display:flex;align-items:center;gap:5px;font-size:8px;font-weight:700;color:#666;margin-top:2px}
.follow-tw span{color:#3a9ad9}
.post{display:flex;gap:8px;font-size:7.5px;line-height:12.5px;color:var(--muted);padding-bottom:5px;margin-bottom:5px;border-bottom:1px solid var(--rule)}
.post:last-child{border-bottom:none}
.thumb{width:32px;height:32px;flex:none;background:linear-gradient(180deg,#6b4a3c,#d9b8a6)}
.post .date{color:var(--red)}
.social{list-style:none;font-size:7.5px;color:var(--muted)}
.social li{display:flex;align-items:center;gap:10px;height:23px}
.sq{width:16px;height:16px;background:#5a5a5a;flex:none}
.news-title{font-family:"Roboto Condensed",sans-serif;font-size:17px;color:var(--red);margin:8px 0 6px}
.newsform{display:flex;gap:4px}
.newsform input{width:162px;height:22px;background:#3a3a3a;border:none;color:#ccc;font-style:italic;font-size:7.5px;padding-left:6px;font-family:"Open Sans",sans-serif}
.newsform button{width:27px;height:22px;background:var(--red);color:var(--white);border:none;font-family:"Roboto Condensed",sans-serif;font-weight:700;font-style:italic;font-size:15px}

/* footer bar */
.footbar{left:0;top:1152px;width:676px;height:48px;background:var(--band)}
.footnav{left:26px;top:1170px;font-size:7.5px;color:#aaa}
.footnav a{color:inherit;text-decoration:none}
.footnav a.active{color:var(--white)}
.footnav i{font-style:normal;margin:0 4px;color:#777}
.copy{left:418px;top:1170px;font-size:8px;color:#ddd}
.footbrand{left:599px;top:1144px;width:58px;height:56px;background:var(--white);font-family:"Roboto Condensed",sans-serif;color:var(--red);font-size:12px;line-height:12px;text-align:center;padding-top:13px}
</style>
</head>
<body>

<header>
  <div class="abs topbar"></div>
  <div class="abs phone">
    <svg class="icon" width="24" height="24" viewBox="0 0 24 24"><path d="M6 3l3 5-2 2c1 3 4 6 7 7l2-2 5 3-2 4C11 22 2 13 2 5z" fill="none" stroke="#9a9a9a" stroke-width="1.6"/></svg>
    418.620.3370
  </div>
  <div class="abs navband"></div>
  <nav class="abs nav">
    <a class="n1 active" href="#">Accueil</a>
    <a class="n2" href="#">Agence</a>
    <a class="n3" href="#">Services Approche</a>
    <a class="n4" href="#">Publications</a>
    <a class="n5" href="#">Contact</a>
  </nav>
</header>

<section>
  <div class="abs hero" role="img" aria-label="Blurred conference room background"></div>
  <div class="abs hero-box" role="img" aria-label="White and red cube bearing the agency name"></div>
  <h1 class="abs hero-title"><span class="thin">Specialised <span class="hl">PR and</span></span><br><span class="hl">communications</span><br><span class="hl">services</span> for<br>customers in the<br>healthcare sector</h1>
</section>
<div class="abs brandtag"><div class="brandname">pellerin<br>dautry</div></div>

<section>
  <h2 class="abs section-head">Our Service</h2>
  <div class="abs tiles">
    <div class="tile-feature">Planification<br>Stratégique</div>
    <div class="t1" role="img" aria-label="Printed communication plan document"></div>
    <div class="t2" role="img" aria-label="Close-up of a coin"></div>
    <div class="t3" role="img" aria-label="Raised hands in an audience"></div>
    <div class="t4" role="img" aria-label="Press microphones"></div>
    <div class="t5" role="img" aria-label="Glass medical equipment"></div>
    <div class="t6" role="img" aria-label="Conference stage with presentation screen"></div>
    <div class="t7" role="img" aria-label="Portrait of the agency president"></div>
  </div>
</section>

<section>
  <div class="abs contact"></div>
  <div class="abs map" role="img" aria-label="Map showing the agency location"></div>
  <div class="abs cinfo">
    <div class="crow"><svg class="icon" width="10" height="12" viewBox="0 0 10 12"><path d="M5 0a4 4 0 014 4c0 3-4 8-4 8S1 7 1 4a4 4 0 014-4z" fill="#888"/><circle cx="5" cy="4" r="1.5" fill="#3a3a3a"/></svg>214, rue des Tilleuls Beloeil-sur-Rive (Québec) J3X 1B8</div>
    <div class="crow"><svg class="icon" width="10" height="10" viewBox="0 0 24 24"><path d="M6 3l3 5-2 2c1 3 4 6 7 7l2-2 5 3-2 4C11 22 2 13 2 5z" fill="#888"/></svg>418.620.3370</div>
    <div class="people">
      <div class="person">
        <div class="pname">Pellerin Dautry, ASC</div>
        <div class="prole">(Présidente)</div>
        <div class="crow"><svg class="icon" width="10" height="7"><rect width="10" height="7" fill="#888"/></svg>pdautry@pdautry.example</div>
        <div class="crow"><svg class="icon" width="10" height="10"><rect x="2" width="6" height="10" rx="1" fill="#888"/></svg>514.300.2187</div>
      </div>
      <div class="person">
        <div class="pname">Maude Lavergne</div>
        <div class="prole">(Coordonnatrice)</div>
        <div class="crow"><svg class="icon" width="10" height="7"><rect width="10" height="7" fill="#888"/></svg>mlavergne@pdautry.example</div>
        <div class="crow"><svg class="icon" width="10" height="10"><rect x="2" width="6" height="10" rx="1" fill="#888"/></svg>514.300.9942</div>
      </div>
    </div>
  </div>
</section>

<section class="abs col col-tweets">
  <h3 class="col-title">Tweests</h3>
  <div class="tweet"><div class="avatar-brand">pellerin dautry</div><div><b>pellerindautry</b>@pellerindautry<br>avant, elle a Canada We caughr soc media<br>has <a href="#">http://lnk.example/5lDti</a><br><span class="date">7 Aug</span></div></div>
  <div class="tweet"><div class="avatar-brand">pellerin dautry</div><div><b>pellerindautry</b>@pellerindautry<br>avant, elle a Canada We caughr soc media<br>has <a href="#">http://lnk.example/5lDti</a><br><span class="date">7 Aug</span></div></div>
  <div class="tweet"><div class="avatar-brand">pellerin dautry</div><div><b>pellerindautry</b>@pellerindautry<br>avant, elle a Canada We caughr soc media<br>has <a href="#">http://lnk.example/5lDti</a><br><span class="date">7 Aug</span></div></div>
  <div class="follow-tw"><svg width="16" height="16"><circle cx="8" cy="8" r="8" fill="#3a9ad9"/></svg>follows us on <span>Chirplet</span></div>
</section>

<section class="abs col col-posts">
  <h3 class="col-title">Latest Post</h3>
  <div class="post"><div class="thumb" role="img" aria-label="Author portrait"></div><div>étentrice d'un baccalauréat en communica-<br>tions et sciences politiques et<br><span class="date">7 Aug</span></div></div>
  <div class="post"><div class="thumb" role="img" aria-label="Author portrait"></div><div>étentrice d'un baccalauréat en communica-<br>tions et sciences politiques et<br><span class="date">7 Aug</span></div></div>
  <div class="post"><div class="thumb" role="img" aria-label="Author portrait"></div><div>étentrice d'un baccalauréat en communica-<br>tions et sciences politiques et<br><span class="date">7 Aug</span></div></div>
  <div class="post"><div class="thumb" role="img" aria-label="Author portrait"></div><div>étentrice d'un baccalauréat en communica-<br>tions et sciences politiques et<br><span class="date">7 Aug</span></div></div>
</section>

<section class="abs col col-follow">
  <h3 class="col-title">Follow us</h3>
  <ul class="social">
    <li><span class="sq"></span>Join us on Friendhub</li>
    <li><span class="sq"></span>Connect with us on Chirplet</li>
    <li><span class="sq"></span>Join us on Circlespot</li>
    <li><span class="sq"></span>Connect with us on Pinboardly</li>
    <li><span class="sq"></span>Join us on Viewtube</li>
    <li><span class="sq"></span>Get our latest RSS updates</li>
  </ul>
  <h3 class="news-title">Newsletter</h3>
  <form class="newsform"><input type="text" placeholder="Email Address..."><button type="button">Go</button></form>
</section>

<footer>
  <div class="abs footbar"></div>
  <nav class="abs footnav"><a class="active" href="#">Accueil</a><i>/</i><a href="#">Agence</a><i>/</i><a href="#">Services</a><i>/</i><a href="#">Approche</a><i>/</i><a href="#">Publications</a><i>/</i><a href="#">Contact</a></nav>
  <div class="abs copy">©2013. Pellerin Dautry. All rights reserved</div>
  <div class="abs footbrand">pellerin<br>dautry</div>
</footer>

</body>
</html>
```